Lacrosse Magazine Ad
Pell9kin
Lacrosse Magazine Ad -
Creative Brief
This magazine ad is about our non-for-profit organization Pell9kin. We want this Pell9kin ad to go along with our "Goal" Campaign. The first 2 ads from this campaign are attached. Pell9kin is an organization that spreads the game of lacrosse throughout Long Island, NY to underprivileged areas that don't have the sport of lacrosse. Pell9kin is a growing project and is always welcoming to those who are willing to help spread the game of lacrosse.
Anyone who is interested in lacrosse and cares about helping spread the game of lacrosse.
**Must say that Pell9kin is the non-for-profit side of Under the Bright Harbor Sky Lacrosse. -Pell9kin logo (attached) -Short and simple description of Pell9kin -Our website - www.pell9kin.example -Have a similar look to our 2 previous ads

```html
<!DOCTYPE html>
<html lang="en">
<head>
<meta charset="utf-8">
<title>Pell9kin – Lacrosse Magazine Ad</title>
<link href="https://fonts.googleapis.com/css2?family=Great+Vibes&family=Open+Sans:wght@400;700&display=swap" rel="stylesheet">
<style>
  :root {
    --ink-black: #000000;
    --navy-top: #0c2550;
    --cyan-glow: #1fc6de;
    --ad-blue: #0a108a;
    --band-blue: #7eafdc;
    --white: #ffffff;
    --link-cyan: #3fb3ea;
    --field-green: #4f7a3a;
    --jersey-blue: #2a55b8;
  }
  html, body {
    margin: 0;
    padding: 0;
    overflow: hidden;
    background: var(--ink-black);
  }
  .canvas {
    position: relative;
    width: 1200px;
    height: 648px;
    overflow: hidden;
    background: linear-gradient(to bottom, var(--navy-top) 0, #123c70 300px, var(--cyan-glow) 500px, var(--cyan-glow) 523px, var(--ink-black) 523px);
    font-family: "Open Sans", sans-serif;
  }
  .ad {
    position: absolute;
    left: 36px;
    top: 29px;
    width: 1128px;
    height: 463px;
    overflow: hidden;
  }
  .ad__top {
    position: absolute;
    left: 0; top: 0;
    width: 100%; height: 211px;
    background: var(--ad-blue);
  }
  .ad__band {
    position: absolute;
    left: 0; top: 211px;
    width: 100%; height: 168px;
    background: var(--band-blue);
  }
  .ad__footer {
    position: absolute;
    left: 0; top: 379px;
    width: 100%; height: 84px;
    background: var(--ink-black);
  }
  .headline {
    position: absolute;
    left: 132px;
    top: 80px;
    margin: 0;
    font-family: "Great Vibes", cursive;
    font-weight: 400;
    font-size: 42px;
    color: var(--white);
    white-space: nowrap;
  }
  .action-photo {
    position: absolute;
    left: 600px;
    top: 4px;
    width: 430px;
    height: 436px;
    border-radius: 50%;
    background:
      radial-gradient(ellipse at 50% 40%, var(--jersey-blue) 0, #31509a 35%, var(--field-green) 62%, rgba(79,122,58,0.55) 72%, rgba(126,175,220,0) 78%);
  }
  .brand-tile {
    position: absolute;
    left: 144px;
    top: 247px;
    width: 168px;
    height: 84px;
    border-radius: 6px;
    background: var(--white);
    display: flex;
    align-items: center;
    justify-content: center;
    font-weight: 700;
    font-size: 26px;
    color: var(--ad-blue);
  }
  .divider {
    position: absolute;
    left: 326px;
    top: 211px;
    width: 3px;
    height: 168px;
    background: var(--white);
  }
  .about {
    position: absolute;
    left: 344px;
    top: 236px;
    width: 244px;
  }
  .tagline {
    margin: 0;
    font-size: 15px;
    line-height: 1.35;
    color: var(--white);
  }
  .description {
    margin: 8px 0 0;
    font-size: 12px;
    line-height: 1.4;
    color: var(--white);
  }
  .visit {
    position: absolute;
    left: 168px;
    top: 402px;
  }
  .visit__label {
    display: block;
    font-size: 10px;
    color: var(--white);
  }
  .visit__url {
    display: block;
    margin-top: 4px;
    font-weight: 700;
    font-size: 15px;
    color: var(--link-cyan);
  }
  .partner-name {
    position: absolute;
    right: 30px;
    top: 396px;
    width: 170px;
    text-align: right;
    font-weight: 700;
    font-size: 13px;
    line-height: 1.3;
    color: var(--white);
  }
</style>
</head>
<body>
<main class="canvas">
  <section class="ad">
    <div class="ad__top"></div>
    <div class="ad__band"></div>
    <div class="ad__footer"></div>

    <div class="action-photo" role="img" aria-label="Youth lacrosse players in blue jerseys battling for a ground ball on a grass field"></div>

    <h1 class="headline">Bright Harbor Sky Lacrosse.</h1>

    <div class="brand-tile">Pell9kin</div>
    <div class="divider"></div>
    <div class="about">
      <p class="tagline">Pell9kin is the non-for-profit side of Under the Bright Harbor Sky Lacrosse.</p>
      <p class="description">We bring lacrosse to underprivileged areas of Long Island, NY. Help us spread the game.</p>
    </div>

    <div class="visit">
      <span class="visit__label">Please Visit us</span>
      <span class="visit__url">www.pell9kin.example</span>
    </div>

    <div class="partner-name">Under the Bright Harbor Sky Lacrosse</div>
  </section>
</main>
</body>
</html>
```